Business Card for Willowcrest Terrain Advisors

We need a business card for Willowcrest Terrain Advisors. The company website address is provided below. The company logo is attached. We provide specialized permafrost services to the mining, transportation, and oil & gas industries. The card should be prepared for:
Dominic Halloway, PhD.
Willowcrest Terrain Advisors
PO Box 418529
Birch Hollow, Alaska 99612
Direct: +1-907-555-2964
Email: dhalloway@terrainadvisors-example.com
Website: www.willowcrestterrainadvisors-example.com

```html
<!DOCTYPE html>
<html lang="en">
<head>
<meta charset="utf-8">
<title>Willowcrest Terrain Advisors – Business Card</title>
<link rel="stylesheet" href="https://fonts.googleapis.com/css2?family=Quicksand:wght@500;600;700&display=swap">
<style>
  :root {
    --backdrop: #aaaaaa;
    --card: #ffffff;
    --ink: #16191d;
    --text: #3a3d42;
    --rule: #9a9da2;
    --shadow: rgba(0, 0, 0, 0.28);
  }
  * { margin: 0; padding: 0; box-sizing: border-box; }
  html, body {
    width: 1200px;
    height: 1000px;
    overflow: hidden;
    background: var(--backdrop);
    font-family: "Quicksand", sans-serif;
  }
  .canvas { position: relative; width: 1200px; height: 1000px; }

  .card {
    position: absolute;
    left: 293px;
    width: 615px;
    height: 354px;
    background: var(--card);
    border-radius: 16px;
    box-shadow: 0 3px 7px var(--shadow);
  }
  .card--front { top: 132px; }
  .card--back { top: 530px; }

  .brand {
    position: absolute;
    color: var(--ink);
    font-weight: 700;
    text-align: center;
    text-transform: uppercase;
    line-height: 1;
  }
  .brand__name { display: block; }
  .brand__sub { display: block; }

  .card--front .brand {
    left: 0; right: 0; top: 163px;
  }
  .card--front .brand__name { font-size: 34px; letter-spacing: 2px; }
  .card--front .brand__sub { font-size: 12.5px; letter-spacing: 3px; margin-top: 8px; }

  .card--back .brand {
    left: 40px; width: 240px; top: 171px;
  }
  .card--back .brand__name { font-size: 23px; letter-spacing: 1.5px; }
  .card--back .brand__sub { font-size: 8.5px; letter-spacing: 2.2px; margin-top: 6px; }

  .divider {
    position: absolute;
    left: 283px; top: 117px;
    width: 1px; height: 144px;
    background: var(--rule);
  }

  .details {
    position: absolute;
    left: 305px; top: 117px;
    color: var(--text);
    font-size: 13px;
    font-weight: 500;
    line-height: 17px;
  }
  .details__name { font-weight: 700; }
  .details__group + .details__group { margin-top: 13px; }
  .contact { list-style: none; font-size: 12.3px; letter-spacing: -0.1px; }
  .contact li { display: flex; align-items: center; gap: 6px; height: 16.5px; }
  .contact svg { width: 12px; height: 12px; flex: none; fill: var(--text); }
</style>
</head>
<body>
<main class="canvas">
  <section class="card card--front" aria-label="Card front">
    <div class="brand">
      <span class="brand__name">Willowcrest</span>
      <span class="brand__sub">Terrain Advisors</span>
    </div>
  </section>

  <section class="card card--back" aria-label="Card back">
    <div class="brand">
      <span class="brand__name">Willowcrest</span>
      <span class="brand__sub">Terrain Advisors</span>
    </div>
    <div class="divider"></div>
    <div class="details">
      <div class="details__group">
        <div class="details__name">Dominic Halloway, PhD.</div>
        <div>Willowcrest Terrain Advisors</div>
      </div>
      <div class="details__group">
        <div>PO Box 418529</div>
        <div>Birch Hollow, Alaska 99612</div>
      </div>
      <ul class="details__group contact">
        <li>
          <svg viewBox="0 0 24 24" aria-hidden="true"><path d="M6.6 10.8a15.2 15.2 0 0 0 6.6 6.6l2.2-2.2c.3-.3.7-.4 1-.2 1.1.4 2.3.6 3.6.6.6 0 1 .4 1 1V20c0 .6-.4 1-1 1A17 17 0 0 1 3 4c0-.6.4-1 1-1h3.5c.6 0 1 .4 1 1 0 1.3.2 2.5.6 3.6.1.3 0 .7-.2 1z"/></svg>
          <span>+1-907-555-2964</span>
        </li>
        <li>
          <svg viewBox="0 0 24 24" aria-hidden="true"><path d="M2 5h20v14H2zm2 2v.5l8 5 8-5V7zm0 2.8V17h16V9.8l-8 5z"/></svg>
          <span>dhalloway@terrainadvisors-example.com</span>
        </li>
        <li>
          <svg viewBox="0 0 24 24" aria-hidden="true"><path d="M12 2a10 10 0 1 0 0 20 10 10 0 0 0 0-20zm6.9 6h-2.9a15.6 15.6 0 0 0-1.4-3.6A8 8 0 0 1 18.9 8zM12 4c.8 1.2 1.5 2.5 1.9 4h-3.8c.4-1.5 1.1-2.8 1.9-4zM4.3 14a8 8 0 0 1 0-4h3.4a16 16 0 0 0 0 4zm.8 2h2.9c.3 1.3.8 2.5 1.4 3.6A8 8 0 0 1 5.1 16zM8 8H5.1a8 8 0 0 1 4.3-3.6C8.8 5.5 8.3 6.7 8 8zm4 12c-.8-1.2-1.5-2.5-1.9-4h3.8c-.4 1.5-1.1 2.8-1.9 4zm2.3-6H9.7a14.7 14.7 0 0 1 0-4h4.6a14.7 14.7 0 0 1 0 4zm.3 5.6c.6-1.1 1.1-2.3 1.4-3.6h2.9a8 8 0 0 1-4.3 3.6zm1.7-5.6a16 16 0 0 0 0-4h3.4a8 8 0 0 1 0 4z"/></svg>
          <span>www.willowcrestterrainadvisors-example.com</span>
        </li>
      </ul>
    </div>
  </section>
</main>
</body>
</html>
```